Stationery including letterhead, business cards, for a new Chartered Accounting Practice

I need a new set of stationery including letterhead, business cards, for a new Chartered Accounting Practice based in Melbourne, Victoria, Australia called "Brint Holloway, Chartered Accountant".

I will be providing Auditing and general consulting advice to small and medium business enterprises. The final design should communicate trust, wisdom and security.

Target Market(s)

Target Market English speaking, Australians. Proprietors small and medium sized businesses - aged 45-65. Fellow professionals - lawyers, investment consultants, other accountants. Retirees - aged 60 and over

Industry/Entity Type

Accountant

Font styles to use
Serif

Colors
0355a3

Requirements
Must have
• The final design should convey trust, wisdom and security.
• Names of practice "Brint Holloway , Chartered Accountant"
• Contact details:
• Address 284 Marbury Street, Tallow Creek, Victoria, 3172, Australia
• Telephone: 047 000 3158
• Email: brintholloway@postquill.example
Nice to have
• an expensive and professional design, the letterhead should be timeless with a logo on white space
Should not have
• no bright/fluro colours

```html
<!DOCTYPE html>
<html lang="en">
<head>
<meta charset="utf-8">
<title>Brint Holloway, Chartered Accountant — Business Cards</title>
<link href="https://fonts.googleapis.com/css2?family=Archivo:wght@700&family=Jost:wght@400&family=Arimo:wght@400;700&display=swap" rel="stylesheet">
<style>
  :root {
    --backdrop: #1c1c1e;
    --card-light: #f6f6f6;
    --card-dark: #161616;
    --ink: #1b1b1b;
    --ink-soft: #2a2a2a;
    --band-grey: #9a9a9a;
    --tone-on-dark: #2c2c2c;
    --tone-on-dark-soft: #282828;
  }
  * { margin: 0; padding: 0; box-sizing: border-box; }
  html, body { width: 1200px; height: 1001px; overflow: hidden; }
  body { background: var(--backdrop); position: relative; }

  .card {
    position: absolute;
    left: 306px;
    width: 589px;
    height: 330px;
    box-shadow: 0 4px 10px rgba(0,0,0,0.45);
    overflow: hidden;
  }
  .card--front { top: 132px; background: var(--card-light); color: var(--ink); }
  .card--back  { top: 540px; background: var(--card-dark); }

  .mark {
    position: absolute;
    left: 50%;
    transform: translateX(-50%);
    width: 58px;
    height: 58px;
  }
  .card--front .mark { top: 66px; background: var(--ink); }
  .card--back .mark  { top: 108px; background: var(--tone-on-dark); }

  .name {
    position: absolute;
    left: 0; right: 0;
    text-align: center;
    font-family: "Archivo", sans-serif;
    font-weight: 700;
    font-size: 26px;
    letter-spacing: 0.3px;
    line-height: 1;
  }
  .title {
    position: absolute;
    left: 0; right: 0;
    text-align: center;
    font-family: "Jost", sans-serif;
    font-size: 11.5px;
    letter-spacing: 0.6px;
    line-height: 1;
  }
  .card--front .name  { top: 159px; }
  .card--front .title { top: 187px; color: var(--ink-soft); }
  .card--back .name   { top: 204px; color: var(--tone-on-dark); }
  .card--back .title  { top: 233px; color: var(--tone-on-dark-soft); }

  .contact {
    position: absolute;
    left: 0; right: 0;
    top: 258px;
    text-align: center;
    font-family: "Arimo", sans-serif;
    font-size: 13px;
    line-height: 19px;
    color: var(--ink);
  }
  .contact strong { font-weight: 700; }

  .base-band { position: absolute; left: 0; bottom: 0; width: 589px; height: 18px; }
</style>
</head>
<body>
  <section class="card card--front">
    <div class="mark"></div>
    <h1 class="name">BRINT HOLLOWAY</h1>
    <p class="title">CHARTERED ACCOUNTANT</p>
    <address class="contact" style="font-style:normal">
      284 Marbury Street, Tallow Creek, Victoria, 3172, Australia<br>
      <strong>Phone:</strong> 047 000 3158 · <strong>Email:</strong> brintholloway@postquill.example
    </address>
    <svg class="base-band" viewBox="0 0 589 18" aria-hidden="true">
      <rect x="0" y="9" width="589" height="9" fill="var(--band-grey)"/>
      <polygon points="64,0 525,0 543,18 46,18" fill="var(--card-light)"/>
      <polygon points="66,0 523,0 539,18 50,18" fill="var(--ink)"/>
    </svg>
  </section>

  <section class="card card--back">
    <div class="mark"></div>
    <p class="name">BRINT HOLLOWAY</p>
    <p class="title">CHARTERED ACCOUNTANT</p>
  </section>
</body>
</html>
```